Business Card Design Project

Thornwick Property Management

Our Business is residential property management, we therefore need a card that displays a professional image, but is clear and concise, and easy to read
Updates

We are committed now guys and girls, loving what we are seeing so far! 

Target Market(s)

Landlords, Rental Property Owners

Industry/Entity Type

Residential

Requirements
Must have
• Dale Thornwick - Principal
Fiona Thornwick - Director (Property Management)

PO Box 817
Pellworth SA 5193

Dale: 0490 367 258
Fiona: 0490 723 519

www.thornwickpropertymanagement.com.au
admin@thornwickpropertymanagement.com.au

Nice to have
• I would like the card to be double sided, white background on the information side and then colour on the reverse, in blue or black and incorporating our logo

```html
<!DOCTYPE html>
<html lang="en">
<head>
<meta charset="utf-8">
<title>Thornwick Property Management – Business Card</title>
<link href="https://fonts.googleapis.com/css2?family=Arimo:wght@400;700&display=swap" rel="stylesheet">
<style>
  :root {
    --page: #d9d9d9;
    --card-black: #050505;
    --pattern-dark: #121212;
    --paper: #f7f7f7;
    --brand-blue: #1a7fc8;
    --ink-grey: #4a4a4a;
    --white: #ffffff;
  }
  * { box-sizing: border-box; margin: 0; padding: 0; }
  html, body {
    width: 1067px; height: 1200px; overflow: hidden;
    background: var(--page);
    font-family: "Arimo", Arial, sans-serif;
  }
  .card {
    position: absolute; left: 103px; width: 860px; height: 525px;
    box-shadow: 0 10px 30px rgba(0,0,0,.35);
    overflow: hidden;
  }
  /* Front side */
  .card--front { top: 50px; background: var(--card-black); }
  .front-pattern {
    position: absolute; inset: 0;
    background: linear-gradient(160deg, var(--pattern-dark), var(--card-black));
  }
  .front-brand {
    position: absolute; left: 0; right: 0; top: 200px;
    display: flex; align-items: center; justify-content: center; gap: 18px;
  }
  .brand-square { width: 70px; height: 56px; background: var(--brand-blue); flex: none; }
  .front-brand .brand-name {
    color: var(--white); font-weight: 700; font-size: 40px; line-height: 1;
  }
  .front-url {
    position: absolute; left: 0; right: 0; top: 335px; text-align: center;
    color: var(--white); font-size: 15px; letter-spacing: 2px; font-weight: 700;
  }
  /* Info side */
  .card--back { top: 625px; background: var(--card-black); }
  .back-top {
    position: absolute; left: 0; top: 0; right: 0; height: 195px;
    background: var(--paper);
  }
  .back-brand {
    position: absolute; left: 60px; top: 62px;
    display: flex; align-items: center; gap: 18px;
  }
  .back-brand .brand-square { width: 86px; height: 68px; }
  .back-brand .brand-name {
    color: var(--ink-grey); font-weight: 700; font-size: 36px; line-height: 1;
  }
  .contact {
    position: absolute; top: 228px; color: var(--white); font-size: 16px; line-height: 1.5;
  }
  .contact--principal { left: 120px; }
  .contact--director { left: 420px; top: 218px; }
  .contact .name { color: var(--brand-blue); font-size: 21px; }
  .contact .role { font-size: 14px; margin-left: 6px; }
  .contact .label { color: var(--brand-blue); margin-right: 6px; }
  .contact .line { margin-left: 16px; }
  .address { margin-top: 22px; margin-left: 16px; }
  .gap { margin-top: 22px; }
</style>
</head>
<body>

<section class="card card--front" aria-label="Card front">
  <div class="front-pattern" role="img" aria-label="Dark repeating brand pattern across the card"></div>
  <div class="front-brand">
    <span class="brand-square"></span>
    <span class="brand-name">Thornwick Property Management</span>
  </div>
  <p class="front-url">www.thornwickpropertymanagement.com.au</p>
</section>

<section class="card card--back" aria-label="Card information side">
  <div class="back-top">
    <div class="back-brand">
      <span class="brand-square"></span>
      <span class="brand-name">Thornwick Property Management</span>
    </div>
  </div>

  <div class="contact contact--principal">
    <p><span class="name">Dale Thornwick</span><span class="role">Principal</span></p>
    <p class="line"><span class="label">p:</span>0490 367 258</p>
    <p class="address">PO Box 817<br>Pellworth SA 5193</p>
  </div>

  <div class="contact contact--director">
    <p><span class="name">Fiona Thornwick</span><span class="role">Director &nbsp;(Property Management)</span></p>
    <p class="line"><span class="label">p:</span>0490 723 519</p>
    <p class="line gap"><span class="label">e:</span>admin@thornwickpropertymanagement.com.au</p>
    <p class="line"><span class="label">w:</span>www.thornwickpropertymanagement.com.au</p>
  </div>
</section>

</body>
</html>
```